'We're just a little bit different' business cards for an IT Startup

We are an Information Technology Start-up focusing on providing IT strategy services to large midcap and enterprise organisations. We need to create business cards which reflect us personally and our brand. Clarvane.io is looking to differentiate itself in the market by providing IT strategy that reflects Information technology today.
We would like business cards that:
- Are just a little bit different, so people read them
- Reflect that Clarvane.Io is a modern disruptive technology company
- Reinforces our brand – strategy reinvented
- Provides information about us that is deeper and richer than just here’s my mobile and email address. We’d like the business card to be a snapshot of who we individually. It might be fav movie, book, sports, favourite beer, my family etc, fav quote etc

I have attached a document which has details about me to use on a sample business card and it also includes snapshots of our website. Also attached is our logo. If you need more information please ask

Industry/Entity Type

Information Technology

Contact Information for Business Card

See attached document, for my personal details to use as a sample

Requirements
Must have
• my details
• web site - url clarvane.io
• something a little bit different
Nice to have
• I'd like to see the design incorporate information about us that lets them see us as fellow human beings not just a work person
Should not have
• standard bland business cards

```html
<!DOCTYPE html>
<html lang="en">
<head>
<meta charset="utf-8">
<title>Clarvane.io business cards</title>
<link href="https://fonts.googleapis.com/css2?family=Arimo:wght@400;700&display=swap" rel="stylesheet">
<style>
  :root {
    --canvas: #6b6259;
    --yellow: #fdc311;
    --yellow-shade: #e8b020;
    --white: #ffffff;
    --charcoal: #343434;
    --charcoal-deep: #252525;
    --ink: #1e1e1e;
    --text-light: #f2f2f2;
  }
  * { box-sizing: border-box; margin: 0; padding: 0; }
  html, body { width: 1200px; height: 1000px; overflow: hidden; }
  body {
    background: var(--canvas);
    font-family: "Arimo", Arial, sans-serif;
    position: relative;
  }
  .card {
    position: absolute;
    width: 660px;
    height: 380px;
    overflow: hidden;
    border-radius: 3px;
    box-shadow: 0 10px 28px rgba(0,0,0,.35);
  }
  .card-art { position: absolute; inset: 0; width: 100%; height: 100%; }

  .brand-name {
    position: absolute;
    transform: translate(-50%, -50%);
    font-weight: 700;
    font-size: 44px;
    letter-spacing: -1px;
    color: var(--ink);
    line-height: 1;
    white-space: nowrap;
  }

  /* front */
  .card-front { left: 110px; top: 80px; background: var(--yellow); }
  .card-front .brand-name { left: 300px; top: 170px; }

  /* back */
  .card-back {
    left: 430px; top: 530px;
    background: linear-gradient(135deg, #3c3c3c 0%, var(--charcoal) 60%, #2d2d2d 100%);
  }
  .card-back .brand-name { left: 205px; top: 200px; }

  .person {
    position: absolute;
    right: 70px; top: 48px;
    text-align: right;
    color: var(--text-light);
  }
  .person-name { font-weight: 700; font-size: 20px; }
  .person-role { font-size: 19px; margin-top: 4px; padding-right: 2px; }
  .contact-list {
    position: absolute;
    right: 34px; top: 190px;
    list-style: none;
    color: var(--text-light);
    font-size: 21px;
  }
  .contact-item {
    display: flex;
    justify-content: flex-end;
    align-items: center;
    gap: 10px;
    margin-bottom: 30px;
  }
  .contact-icon { width: 26px; height: 26px; flex: none; }
</style>
</head>
<body>

  <section class="card card-front" aria-label="Card front">
    <svg class="card-art" viewBox="0 0 660 380" aria-hidden="true">
      <polygon points="170,170 300,290 320,380 60,380" fill="var(--yellow-shade)"/>
      <circle cx="300" cy="170" r="128" fill="var(--white)"/>
    </svg>
    <div class="brand-name">clarvane</div>
  </section>

  <section class="card card-back" aria-label="Card back">
    <svg class="card-art" viewBox="0 0 660 380" aria-hidden="true">
      <polygon points="95,210 310,250 320,380 60,380" fill="var(--charcoal-deep)"/>
      <line x1="330" y1="158" x2="660" y2="158" stroke="var(--yellow)" stroke-width="2"/>
      <circle cx="205" cy="200" r="132" fill="var(--yellow)"/>
    </svg>
    <div class="brand-name">clarvane</div>

    <div class="person">
      <div class="person-name">Marcus Ellery</div>
      <div class="person-role">Founder</div>
    </div>

    <ul class="contact-list">
      <li class="contact-item">
        <span>0411729384</span>
        <svg class="contact-icon" viewBox="0 0 26 26" aria-label="Phone">
          <circle cx="13" cy="13" r="13" fill="var(--yellow)"/>
          <path d="M8.5 7.5c1-.8 2-.6 2.5.3l1 1.8c.4.7.2 1.4-.4 1.8l-.7.5c.6 1.5 1.8 2.7 3.3 3.3l.5-.7c.4-.6 1.1-.8 1.8-.4l1.8 1c.9.5 1.1 1.500.3 2.5-1 1.2-2.6 1.3-4.2.5-2.6-1.3-4.8-3.5-6.1-6.1-.8-1.6-.7-3.2.2-4.5z" fill="var(--charcoal)"/>
        </svg>
      </li>
      <li class="contact-item">
        <span>marcus@clarvane.io</span>
        <svg class="contact-icon" viewBox="0 0 26 26" aria-label="Email">
          <circle cx="13" cy="13" r="13" fill="var(--yellow)"/>
          <rect x="6.5" y="8.5" width="13" height="9" fill="var(--charcoal)"/>
          <polyline points="6.5,8.5 13,13.5 19.5,8.5" fill="none" stroke="var(--yellow)" stroke-width="1.2"/>
        </svg>
      </li>
    </ul>
  </section>

</body>
</html>
```